New website for a commercial real estate consulting company

What we’re looking for in a new web site:
• Desktop and mobile friendly
• Clear navigation
• Strong graphics
• Professional appearance
• The ability to update it ourselves
• Site is for information purposes only – no transactions required
• Traffic counts – number of visits per page?
• A firm quote on costs to develop and launch
• SSL
Attached is a copy of the revised text we propose to use, including our new logo. (The pagination can be different than as shown.)
Our current website address is www.brightlanecounselgroup.ca

```html
<!DOCTYPE html>
<html lang="en">
<head>
<meta charset="utf-8">
<title>Brightlane Counsel Group – Construction Services</title>
<link rel="stylesheet" href="https://fonts.googleapis.com/css2?family=Raleway:wght@400;500;600;700;800&display=swap">
<style>
:root{
  --ink:#111111;
  --white:#ffffff;
  --band-grey:#a6a6a6;
  --band-black:#050505;
  --footer-grey:#8e8e8e;
  --process-brown:#8b7866;
  --logo-navy:#1f2c6b;
  --line:#444444;
}
*{box-sizing:border-box;margin:0;padding:0}
html,body{width:1200px;height:4688px;overflow:hidden}
body{position:relative;background:var(--white);color:var(--ink);font-family:"Raleway",sans-serif}
.abs{position:absolute}
.center{text-align:center}

/* hero */
.hero{left:0;top:0;width:1200px;height:625px;
  background:linear-gradient(135deg,#dcdad7 0%,#f2f1ef 35%,#c9c6c2 60%,#eeedeb 100%)}
.brand{left:234px;top:0;width:188px;height:194px;background:var(--white);
  display:flex;flex-direction:column;align-items:center;justify-content:flex-end;padding-bottom:26px;gap:10px}
.brand-mark{width:40px;height:40px;background:var(--logo-navy)}
.brand-name{font-weight:700;font-size:17px;line-height:1.15;color:var(--logo-navy);text-align:center;letter-spacing:.5px}
.nav{left:509px;top:42px;display:flex;gap:16px;font-weight:800;font-size:19px}
.hero-title{left:0;width:1200px;top:268px;font-weight:700;font-size:47px}
.hero-text{left:350px;width:500px;top:358px;font-size:19px;line-height:1.3}
.hero-btn{left:478px;top:434px;width:244px;height:40px;border:3px solid var(--ink);border-radius:6px;
  font-size:21px;font-weight:500;display:flex;align-items:center;justify-content:center;letter-spacing:.5px}

/* headings */
.section-title{left:0;width:1200px;font-weight:800;font-size:44px}
.body-text{font-size:18px;line-height:1.35}

/* services */
.photo{position:absolute}
.service-label{position:absolute;width:250px;font-weight:800;font-size:17px;text-align:center}

/* experience band */
.band-grey{left:0;top:1375px;width:1200px;height:313px;background:var(--band-grey)}
.years{left:234px;top:1474px;width:220px;font-weight:800;font-size:28px;line-height:1.2}
.years b{font-size:42px;margin-right:10px}
.band-heading{left:466px;top:1392px;font-weight:800;font-size:36px;line-height:1.25}
.band-text{left:466px;top:1508px;width:600px;font-size:22px;line-height:1.35}

/* work band */
.band-black{left:0;top:1688px;width:1200px;height:312px;background:var(--band-black)}
.work-title{left:0;width:1200px;top:1705px;color:var(--white);font-weight:800;font-size:38px}

/* process */
.step-icon{position:absolute;width:119px;height:119px;border-radius:50%;background:var(--process-brown);
  display:flex;align-items:center;justify-content:center}
.step-text{position:absolute;width:140px;font-size:11.5px;font-weight:700;line-height:1.3;text-align:center}

/* team */
.member-name{position:absolute;width:188px;font-weight:800;font-size:29px;text-align:center}
.member-text{position:absolute;width:188px;font-size:18px;line-height:1.3;text-align:center}

/* footer */
.footer{left:0;top:3625px;width:1200px;height:1063px;background:var(--footer-grey)}
.footer-brand{left:234px;top:3650px;font-weight:800;font-size:44px}
.footer-about{left:234px;top:3730px;width:680px;font-size:33px;line-height:1.3;font-weight:500}
.footer-head{font-weight:800;font-size:42px}
.footer-info{font-size:30px;line-height:1.3;font-weight:500}
.news-text{left:590px;top:4144px;width:350px;font-size:22px;line-height:1.35;font-weight:500}
.email-field{left:312px;top:4390px;width:406px;height:63px;border-bottom:2px solid #777;
  font-size:22px;display:flex;align-items:center;padding-left:16px;font-weight:500}
.subscribe{left:738px;top:4390px;width:153px;height:63px;border:3px solid var(--ink);border-radius:8px;
  font-size:22px;display:flex;align-items:center;justify-content:center;font-weight:500}
.follow{left:0;width:1200px;top:4512px;font-weight:700;font-size:30px}
.socials{left:0;width:1200px;top:4572px;display:flex;justify-content:center;gap:32px}
.social-dot{width:26px;height:26px;border-radius:50%;background:var(--ink)}
.copyright{left:0;width:1200px;top:4630px;font-size:22px;font-weight:500}
</style>
</head>
<body>

<header>
  <div class="abs hero" role="img" aria-label="Curved white modern building facade photographed from below"></div>
  <div class="abs brand">
    <div class="brand-mark"></div>
    <div class="brand-name">BRIGHTLANE<br>COUNSEL GROUP</div>
  </div>
  <nav class="abs nav"><span>HOME</span><span>PAGES</span><span>ABOUT US</span><span>SERVICES</span><span>CONTACT</span></nav>
  <h1 class="abs hero-title center">Construction Services</h1>
  <p class="abs hero-text center">It is a long established fact that a reader will be distracted by the readable content of a page when looking at its layout.</p>
  <div class="abs hero-btn">REQUEST A QUOTE</div>
</header>

<section class="services">
  <h2 class="abs section-title center" style="top:736px">OUR SERVICES</h2>
  <p class="abs body-text center" style="left:230px;width:740px;top:808px">It is a long established fact that a reader will be distracted by the readable content of a page when looking at its layout.</p>
  <div class="photo" style="left:278px;top:881px;width:247px;height:157px;background:linear-gradient(135deg,#9a9a9a,#e8e8e8 50%,#3a3a3a)" role="img" aria-label="Modern interior design with white walls and dark accents"></div>
  <div class="photo" style="left:672px;top:881px;width:250px;height:157px;background:linear-gradient(180deg,#8db8dc,#b9cfe0 55%,#a88a5c)" role="img" aria-label="Construction site with cranes under a blue sky"></div>
  <div class="service-label" style="left:276px;top:1064px">Design</div>
  <div class="service-label" style="left:672px;top:1064px">Construction</div>
  <div class="photo" style="left:278px;top:1156px;width:247px;height:157px;background:linear-gradient(135deg,#2b2b2b,#9d9d9d 50%,#1a1a1a)" role="img" aria-label="Steel facade with angled architectural fins"></div>
  <div class="photo" style="left:672px;top:1156px;width:250px;height:157px;background:linear-gradient(135deg,#9fb9d6,#8a6e55 55%,#5a4a3e)" role="img" aria-label="Geodesic sphere building against the sky"></div>
  <div class="service-label" style="left:276px;top:1339px">Renovation</div>
  <div class="service-label" style="left:672px;top:1339px">Architechture</div>
</section>

<section>
  <div class="abs band-grey"></div>
  <div class="abs years center"><b>25</b>YEARS<br>EXPERIENCED</div>
  <h2 class="abs band-heading">We Are A Perfect<br>Construction Solutions</h2>
  <p class="abs band-text">Many desktop publishing packages and web page editors now use Lorem Ipsum as their default model text, and a search for 'lorem ipsum' will uncover many web sites still in their infancy.</p>
</section>

<section>
  <div class="abs band-black"></div>
  <h2 class="abs work-title center">OUR WORK</h2>
  <div class="photo" style="left:253px;top:1778px;width:297px;height:191px;background:linear-gradient(135deg,#b08c6a,#d9d3cb 50%,#7a5f4a)" role="img" aria-label="Workers on scaffolding at a construction site"></div>
  <div class="photo" style="left:650px;top:1778px;width:294px;height:191px;background:linear-gradient(135deg,#cfd8e2,#8d857c 50%,#e4e6ea)" role="img" aria-label="Steel scaffolding frame of a building under construction"></div>
</section>

<section>
  <h2 class="abs section-title center" style="top:2111px">OUR PROCESS</h2>
  <p class="abs body-text center" style="left:310px;width:580px;top:2182px">Lorem Ipsum is simply dummy text of the printing and typesetting industry. Lorem Ipsum has been the industry's standard dummy text ever since the 1500s, when an unknown printer took a galley of type and scrambled it to make a type specimen book.</p>

  <div class="step-icon" style="left:281px;top:2303px"><svg width="44" height="44" viewBox="0 0 44 44"><g fill="#111"><circle cx="10" cy="32" r="5"/><circle cx="22" cy="12" r="5"/><circle cx="34" cy="30" r="5"/></g><path d="M10 32 22 12 34 30" stroke="#111" stroke-width="3" fill="none"/></svg></div>
  <div class="step-icon" style="left:465px;top:2303px"><svg width="44" height="44" viewBox="0 0 44 44"><circle cx="22" cy="22" r="12" stroke="#111" stroke-width="6" stroke-dasharray="5 4" fill="none"/><circle cx="22" cy="22" r="5" fill="#111"/></svg></div>
  <div class="step-icon" style="left:656px;top:2303px"><svg width="44" height="44" viewBox="0 0 44 44"><circle cx="22" cy="22" r="16" fill="#111"/><path d="M14 14c6 2 4 8 10 8s2 8 6 10M28 10c-2 4 2 6 6 6" stroke="#8b7866" stroke-width="3" fill="none"/></svg></div>
  <div class="step-icon" style="left:840px;top:2303px"><svg width="44" height="44" viewBox="0 0 44 44"><circle cx="19" cy="19" r="12" stroke="#111" stroke-width="4" fill="none"/><path d="M28 28 38 38" stroke="#111" stroke-width="5" stroke-linecap="round"/><circle cx="19" cy="19" r="4" fill="#111"/></svg></div>

  <p class="step-text" style="left:271px;top:2444px">It is a long established fact that a reader will be distracted by the readable content of a page when looking at its layout.</p>
  <p class="step-text" style="left:455px;top:2444px">It is a long established fact that a reader will be distracted by the readable content of a page when looking at its layout.</p>
  <p class="step-text" style="left:646px;top:2444px">It is a long established fact that a reader will be distracted by the readable content of a page when looking at its layout.</p>
  <p class="step-text" style="left:830px;top:2444px">It is a long established fact that a reader will be distracted by the readable content of a page when looking at its layout.</p>

  <p class="abs body-text center" style="left:240px;width:720px;top:2584px">Lorem Ipsum is simply dummy text of the printing and typesetting industry. Lorem Ipsum has been the industry's standard dummy text ever since the 1500s, when an unknown printer took a galley of type and scrambled it to make a type specimen book.Lorem Ipsum is simply dummy text of the printing and typesetting industry. Lorem Ipsum has been the industry's standard dummy text ever since the 1500s, when an unknown printer took a galley of type and scrambled it to make a type specimen book.</p>
</section>

<section>
  <h2 class="abs section-title center" style="top:2861px">OUR TEAM</h2>
  <p class="abs body-text center" style="left:280px;width:640px;top:2932px">Lorem Ipsum is simply dummy text of the printing and typesetting industry. Lorem Ipsum has been the industry's standard dummy text ever since the 1500s, when an unknown printer took a galley of type and scrambled it to make a type specimen book.</p>

  <div class="photo" style="left:234px;top:3050px;width:188px;height:156px;background:linear-gradient(180deg,#2a2a2a,#0e0e0e)" role="img" aria-label="Portrait of a team member in a dark suit"></div>
  <div class="photo" style="left:506px;top:3050px;width:188px;height:156px;background:linear-gradient(180deg,#f4f4f4,#cfd3d8)" role="img" aria-label="Portrait of a team member in a navy suit"></div>
  <div class="photo" style="left:778px;top:3050px;width:188px;height:156px;background:linear-gradient(135deg,#6b5a45,#3a2e24 60%,#a58c6a)" role="img" aria-label="Portrait of a team member in a tweed jacket"></div>

  <div class="member-name" style="left:226px;top:3246px">John</div>
  <div class="member-name" style="left:506px;top:3240px">John</div>
  <div class="member-name" style="left:768px;top:3243px">John</div>
  <p class="member-text" style="left:232px;top:3322px">Lorem Ipsum is simply dummy text of the printing and typesetting industry..</p>
  <p class="member-text" style="left:506px;top:3316px">Lorem Ipsum is simply dummy text of the printing and typesetting industry..</p>
  <p class="member-text" style="left:768px;top:3322px">Lorem Ipsum is simply dummy text of the printing and typesetting industry..</p>
</section>

<footer>
  <div class="abs footer"></div>
  <div class="abs footer-brand">Stonemark</div>
  <p class="abs footer-about">Lorem Ipsum is simply dummy text of the printing and typesetting industry. Lorem Ipsum has been the industry's standard dummy text ever since the 1500s, when an unknown printer took a galley of type and scrambled it to make a type specimen book.</p>

  <h3 class="abs footer-head" style="left:234px;top:4045px">Head Office</h3>
  <h3 class="abs footer-head" style="left:590px;top:4045px">Newslatter</h3>
  <p class="abs footer-info" style="left:234px;top:4146px">48 Harbour Lane,<br>Kingsway, Canada</p>
  <p class="abs footer-info" style="left:234px;top:4254px">hello@brightlanecounsel.ca<br>Privacy Policy</p>
  <p class="abs news-text">Subscribe to our newsletter and get the insights &amp; news.</p>

  <div class="abs email-field">Enter Your Email</div>
  <div class="abs subscribe">Subscribe</div>

  <div class="abs follow center">Follow Us</div>
  <div class="abs socials">
    <span class="social-dot" role="img" aria-label="Social network link"></span>
    <span class="social-dot" role="img" aria-label="Social network link"></span>
    <span class="social-dot" role="img" aria-label="Social network link"></span>
    <span class="social-dot" role="img" aria-label="Social network link"></span>
    <span class="social-dot" role="img" aria-label="Social network link"></span>
  </div>
  <p class="abs copyright center">copyright ©&nbsp;&nbsp;&nbsp;&nbsp;All Right Reserved</p>
</footer>

</body>
</html>
```